Flyer for an pediatric sleep consultancy - to distribute to play and childcare centers etc.

I need a flyer that will attract the attention of parents with children between the age of babies to toddlers, who may be experiencing sleep issues. The flyer will be placed at places such as community centers, doctors room, play centers, kindergardens, etc.

My company is called "The Quiet Meadow Studio" and provides a sleep consultancy service. My service essentially provides a customized plan for parents to follow and general advice and guidance. It is not medical advice.

I like to the flyer to have an overall tone that is soft and peaceful with a clean and beautiful design, however can catch the attention of parents who may be struggling with their child's sleep issues and are sleep deprived. I would like photos with minimal text. The colour I use is a brownish rose. I will attach some of my designs to give you an idea. You can have a look at my homepage as well to get an idea about my esthetic direction and the colour. Although the colour of my page is a bit too brownish....

I will provide the text to appear in the flyer once I have a better idea of the layout that I prefer for the flyer. The text however wont be extensive, just some catchy points.

I want to direct people to my website which is www.quietmeadowstudio-example.com
I offer a first FREE evaluation call, to the parents, to get to know each other better, learn about their child's particular sleep problems and see if we are a good fit and can work together. I would like to have this information somehow on the flyer, so that the parents will contact me.
I also have a facebook page, which is: The Quiet Meadow Studio

I have a logo that I would like to appear on the flyer. I will attach the file once the uploader on art bazaar is fixed.

When I print the flyer - I like to print A5 SIZE ... please make sure the formatting is OK for this size.

Here are some text ideas. of course all of it would be too much, I guess. On the front of the flyer I would like to have some catchy phrase or something similar to get people interested and to want to know more. On the back there could be a bit more text and information. But I'm open too suggestions....
I'm not too sure about the wording yet. But here are some text that I might be use:

Is sleep an issue in your home?

Is your baby having trouble sleeping? ... are you?!
I can help!

Sleep, baby, sleep….

Teaching children how to sleep

The Quiet Meadow Studio is a pediatric sleep consultancy that specializes in helping parents with children who struggle to develop good and healthy sleep habits.
Disruptive sleep patterns or not enough sleep can affect the physical, mental and emotional development of your child.

Of course nobody plans to have a sleep problem, but habits can become easily ingrained and spiral quickly out of control and you can find yourself sleep deprived, desperate and not too sure what to do. You see all the other sleeping babies and wish there was someone who understood what you were going through?! Well, there is!

Contact me for a free 15 minute consultation.

This 15 minute „mini“ consultation is a chance to discuss your unique sleep challenges and sleep goals with me. I will provide you with an overview of how I will work with your family to achieve your wildest sleep dreams (goals).
Furthermore do I understand and believe that every child and their family is unique and there is no one size fits all!
I would love to have a chat with you and talk about how I can help make things easier for you and your family!

Do I need a sleep consultant for my child?
The answer is yes if:
- if your child will only fall asleep when nursing or bottle feeding
- if your child needs a dummy or other external aid, like being rocked, patted or taken for a care ride to fall asleep
- if your good night routine is a challenging and exhausting procedure instead of a relaxed and enjoyable moment for the whole family
- if sleep is a constant battle in your home which leaves you feeling frustrated and exhausted
- if your own lack of sleep is taking a toll on you and the whole family

What can I do for you?

I will:

- Guide you to set an age appropriate foundation for good sleep
- Create an individual sleep plan tailored especially to your child’s sleep needs and circumstances
- Help you to teach your childto go to sleep and get back to sleep independently during the night
- show you how to teach your child to take healthful, restorative naps
-Learn

Contact:

Marta Lindqvist
info@quietmeadowstudio-example.com
www.quietmeadowstudio-example.com
+34 612 380 574

Consultations in English, German or Spanish via Phone/Skype or home consultation

Reason: I have to go on a business trip and won't be able to choose a design until the deadline. During the trip I won't have time to give feedback and ask for changes. thank you

Target Market(s)

parents, sleep deprived mothers, young families, child care provider,

Industry/Entity Type

Baby Care

Contact Information for Business Card

Marta Lindqvist
pediatric sleep consultant
+34 612 380 574

```html
<!DOCTYPE html>
<html lang="en">
<head>
<meta charset="utf-8">
<title>The Quiet Meadow Studio – Flyer</title>
<link rel="stylesheet" href="https://fonts.googleapis.com/css2?family=Open+Sans:wght@700&family=Raleway:wght@300&display=swap">
<style>
  :root {
    --rose: #c98b7e;
    --sage-grey: #8b9a95;
    --paper: #ffffff;
    --photo-light: #fbf7f4;
    --photo-skin: #efd3c4;
    --photo-warm: #e3bfae;
    --photo-hair: #d9bf9a;
  }
  * { margin: 0; padding: 0; box-sizing: border-box; }
  html, body { width: 847px; height: 1200px; overflow: hidden; background: var(--paper); }
  .flyer {
    position: relative;
    width: 847px;
    height: 1200px;
    background: var(--paper);
    overflow: hidden;
  }

  /* Brand block */
  .brand {
    position: absolute;
    top: 30px;
    left: 0;
    width: 100%;
    text-align: center;
  }
  .brand-dot {
    display: block;
    width: 70px;
    height: 70px;
    margin: 22px auto 34px;
    border: 2px solid var(--rose);
    border-radius: 50%;
  }
  .brand-name {
    font-family: "Raleway", sans-serif;
    font-weight: 300;
    font-size: 44px;
    color: var(--sage-grey);
    letter-spacing: 0.5px;
    line-height: 1;
  }
  .brand-byline {
    position: absolute;
    top: 200px;
    right: 90px;
    font-family: "Raleway", sans-serif;
    font-weight: 300;
    font-size: 22px;
    color: var(--sage-grey);
  }

  /* Hero photo area */
  .hero-photo {
    position: absolute;
    top: 285px;
    left: 0;
    width: 847px;
    height: 500px;
    background:
      radial-gradient(ellipse 260px 200px at 120px 120px, var(--photo-hair) 0%, transparent 70%),
      radial-gradient(ellipse 300px 220px at 460px 260px, var(--photo-skin) 0%, transparent 75%),
      radial-gradient(ellipse 240px 180px at 220px 170px, var(--photo-warm) 0%, transparent 70%),
      linear-gradient(180deg, var(--photo-light) 0%, #f6ebe4 55%, var(--paper) 100%);
    -webkit-mask-image: linear-gradient(180deg, #000 0%, #000 72%, transparent 100%);
            mask-image: linear-gradient(180deg, #000 0%, #000 72%, transparent 100%);
  }

  /* Headline */
  .headline {
    position: absolute;
    left: 0;
    top: 0;
    font-family: "Open Sans", sans-serif;
    font-weight: 700;
    color: var(--rose);
    font-size: 148px;
    letter-spacing: -5px;
    line-height: 1;
  }
  .headline-line {
    position: absolute;
    white-space: nowrap;
  }
  .headline-line--one { left: 44px; top: 700px; }
  .headline-line--two { left: 196px; top: 830px; }
  .headline-line--three { left: 118px; top: 954px; }

  /* Footer band */
  .footer-band {
    position: absolute;
    left: 0;
    bottom: 0;
    width: 100%;
    height: 73px;
    background: var(--rose);
    display: flex;
    align-items: center;
    justify-content: center;
  }
  .footer-url {
    font-family: "Open Sans", sans-serif;
    font-weight: 700;
    font-size: 19px;
    letter-spacing: 4.6px;
    color: var(--paper);
  }
</style>
</head>
<body>
  <main class="flyer">
    <header class="brand">
      <span class="brand-dot" aria-hidden="true"></span>
      <h1 class="brand-name">The Quiet Meadow Studio</h1>
    </header>
    <p class="brand-byline">by Marta Lindqvist</p>

    <div class="hero-photo" role="img" aria-label="Photo of a mother resting beside her sleeping baby on soft white bedding"></div>

    <h2 class="headline">
      <span class="headline-line headline-line--one">Sleep,</span>
      <span class="headline-line headline-line--two">baby,</span>
      <span class="headline-line headline-line--three">sleep….</span>
    </h2>

    <footer class="footer-band">
      <p class="footer-url">www.quietmeadowstudio-example.com</p>
    </footer>
  </main>
</body>
</html>
```